Business Card Design

We are a flooring/granite/cabinet company
want a sleek and modern design card. Will send our logo. maybe our logo in 3d on card.
black card

Industry/Entity Type

Business

Contact Information for Business Card

Daniel Restrepo
company name Stonecrest Tile Depot
4728 loop 60w 78419
210-647-3928
stonecresttiledepot@mailbarn.net

```html
<!DOCTYPE html>
<html lang="en">
<head>
<meta charset="utf-8">
<title>Stonecrest Tile Depot — Business Card</title>
<link href="https://fonts.googleapis.com/css2?family=Michroma&family=Play:wght@400;700&display=swap" rel="stylesheet">
<style>
  :root {
    --backdrop: #e4e6e9;
    --card: #ffffff;
    --card-shade: #eceef0;
    --navy: #0b4266;
    --band-grey: #c9ccd0;
    --band-light: #dfe1e4;
    --ink: #1c2a36;
    --muted: #4a5560;
  }
  html, body {
    margin: 0;
    width: 1200px;
    height: 900px;
    overflow: hidden;
    background: var(--backdrop);
  }
  .card {
    position: absolute;
    left: 180px;
    top: 210px;
    width: 840px;
    height: 480px;
    border-radius: 48px;
    background: radial-gradient(ellipse at 40% 35%, var(--card) 0%, var(--card-shade) 100%);
    box-shadow: 0 12px 30px rgba(0,0,0,0.14);
    overflow: hidden;
  }
  .card-wave {
    position: absolute;
    inset: 0;
    width: 840px;
    height: 480px;
  }
  .company {
    position: absolute;
    left: 70px;
    top: 205px;
    display: flex;
    align-items: center;
    gap: 14px;
    font-family: "Michroma", sans-serif;
    font-size: 23px;
    color: var(--navy);
    letter-spacing: 1px;
    text-transform: uppercase;
  }
  .company-mark {
    width: 18px;
    height: 18px;
    background: var(--navy);
  }
  .contact {
    position: absolute;
    right: 50px;
    top: 36px;
    text-align: right;
    font-family: "Play", sans-serif;
    color: var(--ink);
  }
  .person-name {
    font-family: "Michroma", sans-serif;
    font-size: 21px;
    font-weight: 400;
    color: var(--navy);
    letter-spacing: 1px;
    text-transform: uppercase;
    margin: 0;
  }
  .person-role {
    font-size: 15px;
    margin: 4px 0 18px;
    color: var(--muted);
  }
  .address {
    font-size: 15px;
    line-height: 20px;
    margin: 0 0 16px;
    text-transform: uppercase;
    letter-spacing: 0.5px;
  }
  .lines {
    list-style: none;
    margin: 0;
    padding: 0;
    font-size: 13px;
  }
  .lines li {
    display: flex;
    justify-content: flex-end;
    align-items: center;
    gap: 8px;
    height: 20px;
  }
  .lines svg {
    width: 13px;
    height: 13px;
    fill: var(--navy);
  }
</style>
</head>
<body>
  <div class="card">
    <svg class="card-wave" viewBox="0 0 840 480" aria-hidden="true">
      <path d="M0,470 C260,452 560,414 840,352 L840,480 L0,480 Z" fill="var(--band-grey)"/>
      <path d="M0,478 C260,462 560,430 840,380 L840,480 L0,480 Z" fill="var(--band-light)"/>
      <path d="M0,388 C260,372 560,362 840,318 L840,342 C560,404 260,442 0,458 Z" fill="var(--navy)"/>
    </svg>

    <div class="company">
      <span class="company-mark"></span>
      <span>Stonecrest Tile Depot</span>
    </div>

    <div class="contact">
      <h1 class="person-name">Daniel Restrepo</h1>
      <p class="person-role">Managing Director</p>
      <p class="address">4728 Loop 60W<br>78419</p>
      <ul class="lines">
        <li>210-647-3928
          <svg viewBox="0 0 16 16"><path d="M3 1h3l1.5 4-2 1.2a8 8 0 0 0 4.3 4.3L11 8.5l4 1.5v3a2 2 0 0 1-2 2A12 12 0 0 1 1 3a2 2 0 0 1 2-2z"/></svg>
        </li>
        <li>210-647-3928
          <svg viewBox="0 0 16 16"><path d="M4 0h8a1 1 0 0 1 1 1v14a1 1 0 0 1-1 1H4a1 1 0 0 1-1-1V1a1 1 0 0 1 1-1zm1 2v10h6V2z"/></svg>
        </li>
        <li>210-647-3928
          <svg viewBox="0 0 16 16"><path d="M4 1h6v4H4zM1 6h14v8H1zm3 2v2h8V8z"/></svg>
        </li>
        <li>stonecresttiledepot@mailbarn.net
          <svg viewBox="0 0 16 16"><path d="M1 3h14v10H1zm1.5 1.5L8 9l5.5-4.5z"/></svg>
        </li>
        <li>www.stonecrestdepot.net
          <svg viewBox="0 0 16 16"><path d="M8 1a7 7 0 1 0 0 14A7 7 0 0 0 8 1zm0 1.5c1 1.2 1.6 2.9 1.7 4.7H6.3C6.4 5.4 7 3.7 8 2.5zM2.6 7.2a5.5 5.5 0 0 1 3-4.2 8 8 0 0 0-1 4.2zm0 1.6h2a8 8 0 0 0 1 4.2 5.5 5.5 0 0 1-3-4.2zM8 13.5c-1-1.2-1.6-2.9-1.7-4.7h3.4c-.1 1.8-.7 3.5-1.7 4.7zm2.4-.5a8 8 0 0 0 1-4.2h2a5.5 5.5 0 0 1-3 4.2zm1-5.8a8 8 0 0 0-1-4.2 5.5 5.5 0 0 1 3 4.2z"/></svg>
        </li>
      </ul>
    </div>
  </div>
</body>
</html>
```